Marrowfield Benefit Advisors Business Card Design

I already placed order for cards through sketch hive.

Double sided- back Navy with White logo and raised silver "swoosh"

```html
<!DOCTYPE html>
<html lang="en">
<head>
<meta charset="utf-8">
<title>Marrowfield Benefit Advisors – Business Card</title>
<link href="https://fonts.googleapis.com/css2?family=Cinzel:wght@600&family=Poppins:wght@400;500&display=swap" rel="stylesheet">
<style>
  :root {
    --navy: #00214a;
    --white: #ffffff;
    --backdrop: #828282;
    --ink: #242424;
    --swoosh: #6a6a6a;
    --rule: #2a2a2a;
  }
  * { margin: 0; padding: 0; box-sizing: border-box; }
  html, body { width: 1093px; height: 1200px; overflow: hidden; }
  body { background: var(--backdrop); position: relative; font-family: "Poppins", sans-serif; }

  .card { position: absolute; width: 579px; height: 357px; overflow: hidden; }
  .card--front { left: 264px; top: 226px; background: var(--white); }
  .card--back { left: 264px; top: 620px; width: 583px; height: 357px; background: var(--navy); }

  .card__wave { position: absolute; inset: 0; width: 100%; height: 100%; }

  .brand { position: absolute; display: flex; align-items: center; }
  .brand__dot { border-radius: 50%; flex: none; }
  .brand__name {
    font-family: "Poppins", sans-serif; font-weight: 500; line-height: 1.1;
    letter-spacing: 0;
  }
  .brand__line { display: block; }

  .card--front .brand { left: 34px; top: 152px; gap: 10px; }
  .card--front .brand__dot { width: 28px; height: 28px; background: var(--navy); }
  .card--front .brand__name { color: var(--navy); font-size: 21px; }

  .card--back .brand { left: 50%; top: 50%; transform: translate(-50%, -50%); gap: 16px; }
  .card--back .brand__dot { width: 48px; height: 48px; background: var(--white); }
  .card--back .brand__name { color: var(--white); font-size: 34px; }

  .divider { position: absolute; left: 302px; top: 84px; width: 1px; height: 175px; background: var(--rule); }

  .contact { position: absolute; left: 324px; top: 84px; color: var(--ink); }
  .contact__name { font-family: "Cinzel", serif; font-weight: 600; font-size: 21px; color: var(--navy); line-height: 1.1; }
  .contact__role { font-size: 16px; line-height: 1.1; }
  .contact__list { list-style: none; margin-top: 18px; }
  .contact__item { display: flex; align-items: center; gap: 6px; font-size: 16.5px; line-height: 21px; }
  .contact__item--web { color: var(--navy); }
  .contact__icon { width: 15px; height: 15px; flex: none; fill: var(--navy); }
  .contact__address { margin-top: 19px; font-size: 16.5px; line-height: 21px; font-style: normal; }
</style>
</head>
<body>

<section class="card card--front" aria-label="Card front">
  <svg class="card__wave" viewBox="0 0 579 357" preserveAspectRatio="none" aria-hidden="true">
    <path d="M0 215 C 40 300, 240 334, 402 334 C 300 330, 60 310, 0 244 Z" fill="var(--swoosh)"/>
    <path d="M0 250 C 60 310, 260 334, 402 334 C 480 334, 540 328, 579 322 L 579 357 L 0 357 Z" fill="var(--navy)"/>
  </svg>

  <div class="brand">
    <span class="brand__dot"></span>
    <span class="brand__name"><span class="brand__line">Marrowfield</span><span class="brand__line">Benefit Advisors</span></span>
  </div>

  <div class="divider"></div>

  <div class="contact">
    <p class="contact__name">ELLIOT VARNER</p>
    <p class="contact__role">Managing Director</p>
    <ul class="contact__list">
      <li class="contact__item">
        <svg class="contact__icon" viewBox="0 0 24 24"><path d="M6.6 10.8a15 15 0 0 0 6.6 6.6l2.2-2.2c.3-.3.7-.4 1-.2 1.1.4 2.3.6 3.6.6.6 0 1 .4 1 1V20c0 .6-.4 1-1 1A17 17 0 0 1 3 4c0-.6.4-1 1-1h3.5c.6 0 1 .4 1 1 0 1.3.2 2.5.6 3.6.1.3 0 .7-.2 1z"/></svg>
        044-555 019 274
      </li>
      <li class="contact__item">
        <svg class="contact__icon" viewBox="0 0 24 24"><path d="M2 5h20v14H2z M3 6l9 7 9-7" fill="var(--navy)" stroke="var(--white)" stroke-width="1.5"/></svg>
        hello@marrowfieldba.com
      </li>
      <li class="contact__item contact__item--web">
        <svg class="contact__icon" viewBox="0 0 24 24"><g fill="none" stroke="var(--navy)" stroke-width="2"><circle cx="12" cy="12" r="10"/><ellipse cx="12" cy="12" rx="4.5" ry="10"/><path d="M2 12h20M4 7h16M4 17h16"/></g></svg>
        www.marrowfieldba.com
      </li>
    </ul>
    <address class="contact__address">17, Larkspur Row, Suite 4<br>31807, Westmere</address>
  </div>
</section>

<section class="card card--back" aria-label="Card back">
  <div class="brand">
    <span class="brand__dot"></span>
    <span class="brand__name"><span class="brand__line">Marrowfield</span><span class="brand__line">Benefit Advisors</span></span>
  </div>
</section>

</body>
</html>
```